Corporate Design für ein Installationsunternehmen
Wir sind mit dem Endergebnis sehr glücklich und zufrieden! Pelle ist auf alle unsere Wünsche und Vorschläge ohne zu zögern und mit viel Geduld eingegangen und wir können seine Arbeit wärmstens empfehlen. Vielen Dank nochmal Pelle für das tolle Design.
Zielgruppe
Wir sind ein Installationsunternehmen im Bereich Gas-, Wasser- und Heizung.
Aufgabenstellung
Das Symbol des Triskele sollte im Logo kreativ integriert werden ( wir sind jedoch offen auch für andere kreative Vorschläge die uns inspirieren).
Sauber, akkurat, symmetrisch und professionell soll es rüber kommen.
Das Symbol soll Vertrauen im Kunden wecken.

```html
<!DOCTYPE html>
<html lang="de">
<head>
<meta charset="utf-8">
<title>Valtero – Geschäftsausstattung</title>
<link href="https://fonts.googleapis.com/css2?family=Exo+2:wght@400;600;800&display=swap" rel="stylesheet">
<style>
  :root {
    --bg: #d4d4d4;
    --paper: #ececec;
    --ink: #1f2633;
    --text: #4a4f58;
    --muted: #6b7079;
    --navy: #262e3b;
    --blue: #2d8ed8;
    --yellow: #d7a423;
    --red: #d7333b;
    --window: #d3d6da;
  }
  html, body {
    margin: 0;
    width: 1200px;
    height: 876px;
    overflow: hidden;
    background: var(--bg);
    font-family: "Exo 2", sans-serif;
  }
  .canvas { position: relative; width: 1200px; height: 876px; }

  .brand { display: flex; align-items: center; gap: 8px; }
  .brand-dot { width: 14px; height: 14px; border-radius: 50%; background: var(--ink); }
  .brand-name { font-weight: 800; color: var(--ink); letter-spacing: 0.06em; font-size: 22px; }

  .letterhead {
    position: absolute; left: 70px; top: 38px;
    width: 566px; height: 800px;
    background: var(--paper);
    box-shadow: 0 6px 18px rgba(0,0,0,.12);
  }
  .letterhead .brand { position: absolute; left: 52px; top: 58px; }
  .letter-body {
    position: absolute; left: 52px; top: 300px; width: 440px;
    font-size: 10.5px; line-height: 1.6; color: var(--text); letter-spacing: .03em;
  }
  .letter-body p { margin: 0 0 12px; }
  .letter-footer {
    position: absolute; left: 52px; right: 40px; top: 640px;
    display: grid; grid-template-columns: 1.4fr 1fr 1fr; gap: 20px;
    font-size: 6.5px; line-height: 1.55; color: var(--muted);
    text-transform: uppercase; letter-spacing: .04em;
  }
  .letter-footer p { margin: 0 0 5px; }
  .contact-row { display: grid; grid-template-columns: 34px 1fr; }
  .accent-bars {
    position: absolute; left: 52px; right: 40px; bottom: 40px;
    display: grid; grid-template-columns: 1.4fr 1fr 1fr; gap: 20px;
  }
  .accent-bar { height: 4px; width: 110px; }
  .accent-bar.blue { background: var(--blue); }
  .accent-bar.yellow { background: var(--yellow); }
  .accent-bar.red { background: var(--red); }

  .envelope-back {
    position: absolute; left: 700px; top: 230px;
    width: 460px; height: 230px; background: var(--navy);
    box-shadow: 0 6px 18px rgba(0,0,0,.14);
  }
  .envelope-front {
    position: absolute; left: 668px; top: 330px;
    width: 460px; height: 230px; background: var(--paper);
    box-shadow: 0 6px 18px rgba(0,0,0,.14);
  }
  .envelope-front .brand { position: absolute; left: 30px; top: 100px; }
  .envelope-front .brand-name { font-size: 18px; }
  .envelope-front .brand-dot { width: 11px; height: 11px; }
  .envelope-window {
    position: absolute; right: 30px; top: 50px;
    width: 180px; height: 70px; border-radius: 8px; background: var(--window);
  }
  .envelope-front .accent-bars {
    left: auto; right: 40px; bottom: 0; width: 300px;
    grid-template-columns: 1fr 1fr 1fr; gap: 20px;
  }
  .envelope-front .accent-bar { width: 86px; }
</style>
</head>
<body>
<main class="canvas">
  <section class="letterhead">
    <div class="brand"><span class="brand-dot"></span><span class="brand-name">VALTERO</span></div>
    <div class="letter-body">
      <p>Dear Sir/ Madam,</p>
      <p>Valtero steht für saubere Installationen im Bereich Gas, Wasser und Heizung. Wir planen, montieren und warten Anlagen mit Sorgfalt und Geduld. Jede Aufgabe wird genau abgestimmt, damit unsere Kunden sich auf verlässliche Technik verlassen können. Gern beraten wir Sie persönlich vor Ort und finden gemeinsam die passende Lösung für Ihr Zuhause.</p>
    </div>
    <footer class="letter-footer">
      <div>
        <p>Technisches Servicezentrum Nordtal<br>Norvea GmbH<br>– Regionales Versorgungszentrum –</p>
        <p>Geschäftsführende Gesellschafter:<br>Lena Kosta / Timo Raske</p>
        <p>Technische Leiterin: Lena Kosta</p>
      </div>
      <div>
        <p>Lindenweg 14<br>04870 Grünfeld</p>
        <div class="contact-row"><span>Telefon:</span><span>01234-56780</span></div>
        <div class="contact-row"><span>Fax:</span><span>01234-56781</span></div>
        <div class="contact-row"><span>E-Mail:</span><span>info@norvea-mail.de</span></div>
        <div class="contact-row"><span>Web:</span><span>www.norvea-mail.de</span></div>
      </div>
      <div>
        <p>Kontoverbindung:</p>
        <p>Steuernummer<br>Nordtaler Genossenschaftsbank<br>IBAN DE00 1234 5678 9012 3456 78<br>BIC: NRTLDE00XXX</p>
      </div>
    </footer>
    <div class="accent-bars">
      <span class="accent-bar blue"></span>
      <span class="accent-bar yellow"></span>
      <span class="accent-bar red"></span>
    </div>
  </section>

  <section class="envelope-back"></section>

  <section class="envelope-front">
    <div class="brand"><span class="brand-dot"></span><span class="brand-name">VALTERO</span></div>
    <div class="envelope-window"></div>
    <div class="accent-bars">
      <span class="accent-bar blue"></span>
      <span class="accent-bar yellow"></span>
      <span class="accent-bar red"></span>
    </div>
  </section>
</main>
</body>
</html>
```